Coffee bag + cups: retail packaging

Our is seeking new packaging for a new coffee shop concept. As part of this we need to design new packaging for our coffee products. For this request, we are seeking design layouts for our retail bags and a cup for to-go coffee. We are working with 3 logo versions (pending final approval).

Please reference this website to see the types of coffee bag packaging options, there's a variety of bag options. We'd like the bag to be a Gusseted Bag, size 3.625 x 9.6 x 2.3125. We want a matte laminated material, not shiny.
https://www.brellumpack.com/

BAG
We'd like to see options of a black bag, blue, and kraft paper. Reference attached example.

Below is the text for our current bags, you can use that for now. I've attached example of bags that I like. We will look to you for design thoughts.

[Front]
Logo
100% Tanzanian
12oz
Dark Roast
Ground

[Back]
Amber Ridge Farms was established in 1989 by Marcus Ellery, son of baseball legend Thomas Ellery, and his family in rural Tanzania.
Today the coffee brand is sourced exclusively from the Ellery farm and other small scale family owned farms in Tanzania and East Africa.
This international coffee initiative is designed to bring a greater share of coffee revenues to farmers through direct trade and help develop rural communities in East Africa.

Visit us at Kelvorabeans.com

[Left panel]

Brewing instructions: Lorem ipsum dolor sit amet, consectetur adipiscing elit, sed do eiusmod tempor incididunt ut labore et dolore magna aliqua.

[Right panel]

Leave blank

Cup Sleeve
[Front of sleeve]
Logo

To-go cup
[Front]
Logo

Target Market(s)

Specialty coffee lovers.

Font styles to use
Serif
Sans Serif

Colors

Designer to choose colors to be used in the design.

Requirements
Must have
• Examples of coffee bag packaging.
• Must have; logo, text, clear and elegant labeling. Simple but strong.

```html
<!DOCTYPE html>
<html lang="en">
<head>
<meta charset="utf-8">
<title>Kelvora Coffee – Tanzania Packaging</title>
<link href="https://fonts.googleapis.com/css2?family=Oswald:wght@300;400;500&display=swap" rel="stylesheet">
<style>
  :root {
    --backdrop: #ececec;
    --pack-black: #151515;
    --pack-shade: #1d1d1d;
    --lid-black: #0e0e0e;
    --ink-white: #ffffff;
    --font-main: "Oswald", sans-serif;
  }
  * { margin: 0; padding: 0; box-sizing: border-box; }
  html, body { width: 1200px; height: 923px; overflow: hidden; }
  body {
    background: var(--backdrop);
    font-family: var(--font-main);
    color: var(--ink-white);
    position: relative;
  }

  /* ---------- To-go cup ---------- */
  .cup { position: absolute; left: 242px; top: 346px; width: 262px; height: 450px; z-index: 2; }
  .cup-lid {
    position: absolute; left: 0; top: 0; width: 262px; height: 60px;
    background: var(--lid-black);
    clip-path: polygon(7% 0, 93% 0, 96% 55%, 100% 62%, 100% 100%, 0 100%, 0 62%, 4% 55%);
  }
  .cup-body {
    position: absolute; left: 12px; top: 60px; width: 238px; height: 390px;
    background: linear-gradient(90deg, var(--pack-black), var(--pack-shade) 55%, var(--pack-black));
    clip-path: polygon(0 0, 100% 0, 93% 100%, 7% 100%);
  }

  /* ---------- Retail bag ---------- */
  .bag {
    position: absolute; left: 512px; top: 118px; width: 392px; height: 694px;
    background: linear-gradient(120deg, var(--pack-black), var(--pack-shade) 60%, var(--pack-black));
    border-radius: 4px;
  }
  .bag-notch { position: absolute; top: 0; left: 0; right: 0; height: 14px; border-bottom: 1px solid #222; }

  /* ---------- Brand badge ---------- */
  .brand-badge {
    position: absolute; border: 3px solid var(--ink-white); border-radius: 50%;
    background: var(--pack-black);
    display: flex; align-items: center; justify-content: center;
    font-weight: 400; letter-spacing: 2px; text-transform: uppercase; text-align: center;
    line-height: 1.2; z-index: 2;
  }
  .cup .brand-badge { left: 87px; top: 105px; width: 114px; height: 114px; font-size: 14px; }
  .bag .brand-badge { left: 105px; top: 124px; width: 126px; height: 126px; font-size: 15px; }

  /* ---------- Label frame ---------- */
  .label-frame {
    position: absolute; border: 2.5px solid var(--ink-white); border-radius: 12px;
    text-align: center;
  }
  .cup .label-frame { left: 63px; top: 217px; width: 143px; height: 138px; padding-top: 50px; }
  .bag .label-frame { left: 79px; top: 237px; width: 180px; height: 308px; padding-top: 78px; }

  .origin { font-weight: 500; letter-spacing: 1px; line-height: 1; }
  .cup .origin { font-size: 29px; }
  .bag .origin { font-size: 36px; }
  .purity { font-weight: 300; letter-spacing: 2px; line-height: 1.1; }
  .cup .purity { font-size: 15px; }
  .bag .purity { font-size: 17px; }

  .rule { display: flex; justify-content: center; gap: 8px; margin: 8px auto 0; }
  .rule span { display: block; width: 64px; height: 2px; background: var(--ink-white); }

  .spec-row { display: flex; justify-content: center; margin-top: 26px; text-align: left; }
  .spec { padding: 0 8px; font-size: 16px; line-height: 1.25; }
  .spec + .spec { border-left: 1.5px solid var(--ink-white); }
  .spec-label { font-weight: 300; }
  .spec-value { font-weight: 500; }
  .scoop { display: block; margin: 6px 0 0 22px; }

  .net-weight { margin-top: 34px; font-size: 13px; font-weight: 300; line-height: 1.3; }
</style>
</head>
<body>

<div class="cup" role="img" aria-label="Black to-go cup with a faint coffee bean pattern">
  <div class="cup-lid"></div>
  <div class="cup-body"></div>
  <div class="brand-badge">Kelvora<br>Coffee</div>
  <div class="label-frame">
    <div class="origin">TANZANIA</div>
    <div class="purity">100% PURE</div>
  </div>
</div>

<div class="bag" role="img" aria-label="Matte black gusseted coffee bag with a faint coffee bean pattern">
  <div class="bag-notch"></div>
  <div class="brand-badge">Kelvora<br>Coffee</div>
  <div class="label-frame">
    <div class="origin">TANZANIA</div>
    <div class="purity">100% PURE</div>
    <div class="rule"><span></span><span></span></div>
    <div class="spec-row">
      <div class="spec"><div class="spec-label">ROAST:</div><div class="spec-value">DARK</div></div>
      <div class="spec">
        <div class="spec-value">GROUND</div>
        <svg class="scoop" width="22" height="14" viewBox="0 0 22 14" aria-hidden="true">
          <path d="M1 2 L9 6" stroke="#fff" stroke-width="1.5" fill="none"/>
          <path d="M9 4 L20 7 L18 13 L8 10 Z" stroke="#fff" stroke-width="1.5" fill="none"/>
        </svg>
      </div>
    </div>
    <div class="net-weight">nett. wt.:<br>12oz</div>
  </div>
</div>

</body>
</html>
```